Quillstone Business Card

We need a business card design. We have a logo from a previous Sketchfold project and I am attaching the logo files in jpeg and photoshop.

```html
<!DOCTYPE html>
<html lang="en">
<head>
<meta charset="utf-8">
<title>Quillstone Business Card</title>
<link href="https://fonts.googleapis.com/css2?family=Nunito+Sans:wght@400;600;800&display=swap" rel="stylesheet">
<style>
  :root {
    --bg-dark: #2a2a2a;
    --bg-band: #363636;
    --stripe-light: #e4e4e4;
    --stripe-mid: #bdbdbd;
    --green: #5cb82f;
    --white: #ffffff;
    --text-light: #f2f2f2;
  }
  * { margin: 0; padding: 0; box-sizing: border-box; }
  html, body {
    width: 1200px;
    height: 720px;
    overflow: hidden;
    background: var(--bg-dark);
  }
  .card {
    position: relative;
    width: 1200px;
    height: 720px;
    background: var(--bg-dark);
    font-family: "Nunito Sans", Arial, sans-serif;
    color: var(--text-light);
  }
  .person {
    position: absolute;
    left: 880px;
    top: 96px;
    width: 200px;
    text-align: center;
  }
  .person-name {
    font-size: 39px;
    font-weight: 400;
    color: var(--white);
    letter-spacing: 0.5px;
    line-height: 1.1;
  }
  .person-role {
    margin-top: 10px;
    font-size: 19px;
    color: var(--green);
    line-height: 1;
  }
  .brand {
    position: absolute;
    left: 100px;
    top: 262px;
    display: flex;
    align-items: center;
    gap: 22px;
  }
  .brand-mark {
    width: 62px;
    height: 62px;
    background: var(--green);
  }
  .brand-name {
    font-size: 84px;
    font-weight: 800;
    color: var(--white);
    line-height: 1;
    letter-spacing: -1px;
  }
  .contact-band {
    position: absolute;
    left: 0;
    top: 432px;
    width: 1200px;
    height: 168px;
    background: var(--bg-band);
  }
  .contact-item {
    position: absolute;
    display: flex;
    align-items: flex-start;
    font-size: 19px;
    line-height: 27px;
    color: var(--text-light);
  }
  .contact-item svg {
    flex: none;
    margin-right: 14px;
    margin-top: 1px;
  }
  .address { left: 80px; top: 48px; text-transform: uppercase; }
  .address svg { margin-right: 17px; }
  .phone { left: 462px; top: 47px; }
  .fax { left: 462px; top: 91px; }
  .web { left: 822px; top: 46px; }
  .mail { left: 822px; top: 89px; }
  .phone span, .fax span { margin-left: 14px; }
  .stripe {
    position: absolute;
    left: 0;
    top: 600px;
    width: 1200px;
    height: 28px;
    background: var(--stripe-light);
    border-top: 10px solid var(--stripe-mid);
  }
</style>
</head>
<body>
  <div class="card">
    <div class="person">
      <div class="person-name">Ravin K</div>
      <div class="person-role">Designer</div>
    </div>

    <div class="brand">
      <div class="brand-mark"></div>
      <div class="brand-name">Quillstone</div>
    </div>

    <div class="contact-band">
      <div class="contact-item address">
        <svg width="20" height="28" viewBox="0 0 20 28" aria-hidden="true">
          <path d="M10 1C5 1 1 5 1 10c0 7 9 17 9 17s9-10 9-17c0-5-4-9-9-9z" fill="var(--green)"/>
          <circle cx="10" cy="10" r="3.5" fill="var(--bg-band)"/>
        </svg>
        <div>Business Name<br>1234 Street Name<br>City, State 12345</div>
      </div>

      <div class="contact-item phone">
        <svg width="16" height="26" viewBox="0 0 16 26" aria-hidden="true">
          <path d="M4 1h6v7H7c-1 3-1 7 0 10h3v7H4C0 19 0 7 4 1z" fill="var(--green)"/>
        </svg>
        <span>+91 123456789</span>
      </div>

      <div class="contact-item fax">
        <svg width="26" height="24" viewBox="0 0 26 24" aria-hidden="true">
          <rect x="7" y="1" width="12" height="7" fill="none" stroke="var(--green)" stroke-width="2"/>
          <rect x="1" y="9" width="24" height="9" rx="1" fill="var(--green)"/>
          <rect x="5" y="18" width="16" height="5" fill="none" stroke="var(--green)" stroke-width="2"/>
        </svg>
        <span>+91 123456789</span>
      </div>

      <div class="contact-item web">
        <svg width="26" height="26" viewBox="0 0 26 26" aria-hidden="true">
          <circle cx="13" cy="13" r="12" fill="var(--green)"/>
          <path d="M6 8c3-1 5 1 6 3s-1 4-3 4-2 3-1 5M17 5c-2 2 0 4 2 4s3 3 1 5-1 4-3 5" fill="none" stroke="var(--bg-band)" stroke-width="2"/>
        </svg>
        <span>www.yourwebsite.com</span>
      </div>

      <div class="contact-item mail">
        <svg width="26" height="26" viewBox="0 0 26 26" aria-hidden="true">
          <rect x="2" y="6" width="22" height="15" fill="none" stroke="var(--green)" stroke-width="2"/>
          <path d="M2 6l11 9 11-9M2 21l8-7M24 21l-8-7" fill="none" stroke="var(--green)" stroke-width="2"/>
        </svg>
        <span>ravin@email.com</span>
      </div>
    </div>

    <div class="stripe"></div>
  </div>
</body>
</html>
```